Need Eye Catching For Sale By Owner Signs

In need of a Eye Catching For Sale By Owner Sign design. I plan on using the sign to market buildings and raw land that I own. The design should be able to scale to different rectangular dimensions for example a yard stake sign or a large 4' x 6' sign to be tacked to plywood. The design should have a dead space near the bottom that I can insert more detail information into at a later time.

The main tag line "For Sale By Owner" and the contact number "319-562-4097" needs to be easily be read from a distance.

```html
<!DOCTYPE html>
<html lang="en">
<head>
<meta charset="utf-8">
<title>For Sale By Owner Sign</title>
<link rel="stylesheet" href="https://fonts.googleapis.com/css2?family=Source+Sans+3:wght@400&display=swap">
<style>
  :root {
    --ink: #000000;
    --paper: #ffffff;
    --signal-red: #ed1c24;
    --art-light: #f4f4f4;
    --art-mid: #e6e6e6;
  }
  html, body {
    margin: 0;
    padding: 0;
    width: 1200px;
    height: 800px;
    overflow: hidden;
    background: var(--paper);
  }
  .sign {
    display: block;
    width: 1200px;
    height: 800px;
    font-family: "Source Sans 3", "Myriad Pro", Arial, sans-serif;
  }
  .house-art-top { stop-color: var(--art-light); }
  .house-art-bottom { stop-color: var(--art-mid); }
  .headline, .subline, .phone { fill: var(--ink); font-weight: 400; }
  .headline { font-size: 265px; }
  .subline { font-size: 112px; }
  .phone { font-size: 126px; }
  .info-band { fill: var(--signal-red); }
  .info-text { fill: var(--paper); font-size: 28px; }
</style>
</head>
<body>
<svg class="sign" viewBox="0 0 1200 800" xmlns="http://www.w3.org/2000/svg" aria-label="For Sale By Owner sign">
  <defs>
    <linearGradient id="house-art-fill" x1="0" y1="0" x2="0" y2="1">
      <stop class="house-art-top" offset="0"/>
      <stop class="house-art-bottom" offset="1"/>
    </linearGradient>
  </defs>

  <rect class="house-art" x="220" y="40" width="980" height="485" fill="url(#house-art-fill)"
        role="img" aria-label="Line drawing of a house outline with a roof and red chimney framing the headline"/>

  <text class="headline" x="78" y="393" textLength="795" lengthAdjust="spacingAndGlyphs">For Sale</text>
  <text class="subline" x="405" y="491" textLength="502" lengthAdjust="spacingAndGlyphs">By Owner</text>
  <text class="phone" x="340" y="657" textLength="817" lengthAdjust="spacingAndGlyphs">(319) 562 - 4097</text>

  <rect class="info-band" x="0" y="700" width="1200" height="100"/>
  <text class="info-text" x="29" y="761" textLength="1142" lengthAdjust="spacingAndGlyphs">More information goes here - More information goes here - more information goes</text>
</svg>
</body>
</html>
```